Prestige Car Bodyshop Business Card

We are a car bodyshop based in the UK. Our customer base is mainly prestige high-value vehicles. I am looking for a classy and stylish business card design for my staff to give out to customers, with their direct email and phone number, as well as our main email and phone number with address details

I am also looking to have a general business card design with just our main company address and contact details, but also have a space to add a manufacturer approval logo (i.e Velmora, Orek, Tovalo etc... logo) in the corner somewhere.

I do not particularly want any outlines or pictures of cars on the card, I would just like a quality high-end look.

Please feel free to get in touch if you have any questions or queries?

Many Thanks

Malcolm

Target Market(s)

Prestige vehicle owners

Industry/Entity Type

Automotive

Contact Information for Business Card

I am looking for a classy and stylish business card design for my staff to give out to customers, with their direct email and phone number, as well as our main email and phone number with address details

Font styles to use
Sans Serif

Colors

Designer to choose colors to be used in the design.

Requirements
Nice to have
• I do not particularly want any outlines or pictures of cars on the card, I would just like a quality high-end look.

```html
<!DOCTYPE html>
<html lang="en">
<head>
<meta charset="utf-8">
<title>Halden Accident Repair Centre – Business Cards</title>
<link href="https://fonts.googleapis.com/css2?family=Comfortaa:wght@400;600&family=Open+Sans:wght@300;400;600&display=swap" rel="stylesheet">
<style>
  :root{
    --bg:#e9ecec;
    --card:#ffffff;
    --navy:#123f7e;
    --blue:#1f68b4;
    --sky:#3c92d3;
    --orange:#f07f1c;
    --grey:#a9adb1;
    --text-blue:#2a6fbf;
  }
  *{margin:0;padding:0;box-sizing:border-box}
  html,body{width:1200px;height:900px;overflow:hidden;background:var(--bg);font-family:"Open Sans",sans-serif}
  .sheet{width:1200px;height:900px;display:flex;flex-direction:column;align-items:center;justify-content:center;gap:50px}
  .card{position:relative;width:600px;height:343px;background:var(--card);box-shadow:0 6px 18px rgba(0,0,0,.12);overflow:hidden}
  .brand-band{position:absolute;left:0;right:0;bottom:0;height:10px;display:flex}
  .brand-band span{height:100%}
  .band-navy{flex:42;background:var(--navy)}
  .band-blue{flex:22;background:var(--blue)}
  .band-sky{flex:18;background:var(--sky)}
  .band-orange{flex:18;background:var(--orange)}

  .company{display:flex;align-items:center;gap:14px}
  .company-dot{width:66px;height:66px;border-radius:50%;background:var(--navy);flex:none}
  .company-name{font-family:"Open Sans",sans-serif;font-weight:300;color:var(--navy);font-size:34px;line-height:1;letter-spacing:1px;padding-bottom:5px;border-bottom:1.5px solid var(--navy)}
  .company-tag{font-family:"Open Sans",sans-serif;font-weight:300;color:var(--navy);font-size:9.5px;letter-spacing:1.2px;margin-top:5px}

  /* front */
  .card-front .company{position:absolute;left:150px;top:118px}
  .partners{position:absolute;left:380px;top:112px;display:flex;flex-direction:column;gap:14px}
  .partner{font-family:"Open Sans",sans-serif;font-weight:300;color:var(--grey);font-size:15px;letter-spacing:1px}

  /* back */
  .card-back .company{position:absolute;left:34px;top:44px}
  .card-back .company-dot{width:58px;height:58px}
  .card-back .company-name{font-size:28px}
  .card-back .company-tag{font-size:8.5px}
  .person{position:absolute;right:40px;top:44px;text-align:right}
  .person-name{font-family:"Comfortaa",sans-serif;font-weight:600;color:var(--text-blue);font-size:22px;letter-spacing:3px}
  .person-role{font-family:"Open Sans",sans-serif;color:var(--text-blue);font-size:11px;margin-top:2px}
  .divider{position:absolute;left:60px;right:40px;top:140px;height:1px;background:var(--text-blue)}
  .contact{position:absolute;list-style:none;color:var(--text-blue);font-size:12.5px}
  .contact li{display:flex;align-items:center;gap:10px;height:22px}
  .contact svg{width:13px;height:13px;flex:none}
  .contact-phones{left:150px;top:190px}
  .contact-online{right:40px;top:160px}
  .contact-online li{justify-content:flex-end}
</style>
</head>
<body>
<main class="sheet">

  <section class="card card-front" aria-label="Business card front">
    <div class="company">
      <span class="company-dot"></span>
      <div>
        <div class="company-name">HALDEN</div>
        <div class="company-tag">ACCIDENT REPAIR CENTRE</div>
      </div>
    </div>
    <div class="partners" aria-label="Manufacturer approvals">
      <span class="partner">Orek</span>
      <span class="partner">Velmora</span>
      <span class="partner">Tovalo</span>
    </div>
    <div class="brand-band"><span class="band-navy"></span><span class="band-blue"></span><span class="band-sky"></span><span class="band-orange"></span></div>
  </section>

  <section class="card card-back" aria-label="Business card back">
    <div class="company">
      <span class="company-dot"></span>
      <div>
        <div class="company-name">HALDEN</div>
        <div class="company-tag">ACCIDENT REPAIR CENTRE</div>
      </div>
    </div>
    <div class="person">
      <div class="person-name">Malcolm Malcolm</div>
      <div class="person-role">founder and CEO</div>
    </div>
    <div class="divider"></div>

    <ul class="contact contact-phones">
      <li>
        <svg viewBox="0 0 16 16" aria-hidden="true"><path fill="var(--orange)" d="M3 1h3l1.5 4-2 1.2a9 9 0 0 0 4.3 4.3L11 8.5l4 1.5v3a2 2 0 0 1-2 2A12 12 0 0 1 1 3a2 2 0 0 1 2-2z"/></svg>
        (204) 555-0142
      </li>
      <li>
        <svg viewBox="0 0 16 16" aria-hidden="true"><rect x="4" y="1" width="8" height="14" rx="1.5" fill="var(--orange)"/><rect x="5.5" y="3" width="5" height="8" fill="#fff"/><circle cx="8" cy="13" r=".9" fill="#fff"/></svg>
        (204) 555-0187
      </li>
    </ul>

    <ul class="contact contact-online">
      <li>Address: Brookfield, MB Canada</li>
      <li>
        <svg viewBox="0 0 16 16" aria-hidden="true"><rect x="1" y="3" width="14" height="10" rx="1" fill="none" stroke="var(--orange)" stroke-width="1.5"/><path d="M1.5 3.5 8 9l6.5-5.5" fill="none" stroke="var(--orange)" stroke-width="1.5"/></svg>
        info@haldenrepair.net
      </li>
      <li>
        <svg viewBox="0 0 16 16" aria-hidden="true"><circle cx="8" cy="8" r="6.5" fill="none" stroke="var(--orange)" stroke-width="1.5"/><path d="M1.5 8h13M8 1.5c-3 3.5-3 9.5 0 13M8 1.5c3 3.5 3 9.5 0 13" fill="none" stroke="var(--orange)" stroke-width="1.2"/></svg>
        www.haldenrepair.com
      </li>
    </ul>

    <div class="brand-band"><span class="band-navy"></span><span class="band-blue"></span><span class="band-sky"></span><span class="band-orange"></span></div>
  </section>

</main>
</body>
</html>
```